Insurance Agency Flyer
8.5 x 11 Double Sided Full Color
Bluelanem your draft #10 is good except that due to trademark issues we must display the insurance company logos across the bottom on a white background only. The overall design is sleek but the blue background under the logos would be a deal breaker. I like the idea of using a house and car also but not that particular house, car and people. Good examples of the kinds of photos we are seeking are those seen in draft #5 and draft #6
@PH - please check your private message on right top once you login.
Thanks
Ravenwood, draft #3 is good. Can you try changing the font color and/or size and/or style of certain words in the "why are you paying so much for auto insurance" line? For example in draft #2, auto insurance stands out more because it is in a different color. I would be curious to see what other options there are to make those words stand out.
Tobel, I like draft #2 however can you make the following modifications:
1. Please note that while we are allowed to use the "Lakemount" logo we can't use their symbols for the Auto, home, motorcycle... etc. Could you replace those symbols with something similar?
2. The CMQ logo should be placed somewhere else as this is not one of our insurance but rather an organization we belong to (for example in draft #1 it is listed on the bottom right).
3. Also, could our phone number be more pronounced somewhere?
4. And finally, I like the overall clean layout but not crazy about that particular guy and car. Any other options?
Ravnewood, I really like draft #1. I would be inetrested to see how it might look if the auto, home, motorcycle... icons were also across the very top of page 1? Also, Is there a way to put more emphasis on the words "auto insurance" justs o that they stand out more, maybe more than the "Paying so Much".

```html
<!DOCTYPE html>
<html lang="en">
<head>
<meta charset="utf-8">
<title>KRV Coverage Agency – Flyer</title>
<link rel="stylesheet" href="https://fonts.googleapis.com/css2?family=Arimo:ital,wght@0,400;0,700;1,700&family=PT+Serif:wght@700&family=Roboto+Condensed:ital,wght@1,700;1,900&display=swap">
<style>
  :root {
    --backdrop: #2b2b2b;
    --white: #ffffff;
    --navy: #0f2f5e;
    --blue: #1d5fa6;
    --blue-deep: #154b8a;
    --blue-light: #3b8fd6;
    --sky-top: #2f7fc6;
    --sky-low: #cfe6f6;
    --yellow: #f7d21c;
    --gold: #e3a21a;
    --grey-text: #3d4a5c;
  }
  * { margin: 0; padding: 0; box-sizing: border-box; }
  html, body { width: 1200px; height: 770px; overflow: hidden; background: var(--backdrop); }
  body { position: relative; font-family: "Arimo", Arial, sans-serif; }

  .page { position: absolute; top: 14px; width: 574px; height: 740px; background: var(--white); overflow: hidden; }
  .page-front { left: 19px; }
  .page-back { left: 610px; }

  /* coverage icon strips */
  .coverage-strip { position: absolute; left: 0; width: 100%; display: flex; justify-content: space-around; align-items: center; }
  .coverage-strip .item { display: flex; flex-direction: column; align-items: center; font-size: 7px; font-weight: 700; letter-spacing: .5px; }
  .coverage-strip svg { width: 34px; height: 20px; }
  .strip-top { top: 0; height: 40px; background: linear-gradient(var(--blue-deep), var(--blue)); color: var(--white); fill: var(--white); }
  .strip-dark { top: 518px; height: 58px; background: linear-gradient(var(--blue-light), var(--blue-deep)); color: var(--white); fill: var(--white); }

  /* front hero */
  .hero { position: absolute; top: 40px; left: 0; width: 100%; height: 486px; background: linear-gradient(var(--sky-top), var(--sky-low)); }
  .headline { position: absolute; top: 26px; width: 100%; text-align: center; font-family: "Roboto Condensed", Arial, sans-serif; font-style: italic; font-weight: 900; text-transform: uppercase; line-height: 1.05; text-shadow: 1px 2px 3px rgba(0,0,0,.35); }
  .headline .line-one { font-size: 27px; color: var(--white); }
  .headline .line-two { font-size: 36px; color: var(--white); }
  .headline .accent { color: var(--yellow); }
  .tagline-arc { position: absolute; top: 90px; left: 0; width: 574px; height: 90px; }
  .tagline-arc text { font-family: "Arimo", Arial, sans-serif; font-style: italic; font-weight: 700; font-size: 20px; fill: var(--white); }
  .hero-photo { position: absolute; top: 128px; left: 0; width: 100%; height: 358px;
    background: linear-gradient(100deg, rgba(232,214,184,.95) 0%, rgba(240,226,205,.9) 45%, rgba(74,106,160,.95) 75%, rgba(160,188,214,.9) 100%);
    -webkit-mask: linear-gradient(transparent 0, #000 60px); mask: linear-gradient(transparent 0, #000 60px); }

  /* front footer */
  .front-footer { position: absolute; top: 526px; left: 0; width: 100%; height: 214px; background: var(--white); }
  .method { position: absolute; left: 22px; top: 16px; width: 300px; color: var(--blue); font-size: 14px; line-height: 21px; }
  .method h3 { color: var(--navy); font-size: 14.5px; font-weight: 700; margin-bottom: 2px; }
  .method ul { list-style: none; }
  .promise { position: absolute; left: 22px; bottom: 16px; color: var(--blue-deep); font-size: 15px; font-weight: 700; line-height: 20px; }
  .brand { position: absolute; display: flex; align-items: center; gap: 10px; color: var(--navy); font-family: "PT Serif", Georgia, serif; font-weight: 700; }
  .brand .dot { width: 14px; height: 14px; border-radius: 50%; background: var(--blue); flex: none; }
  .front-footer .brand { left: 340px; top: 60px; font-size: 20px; line-height: 24px; width: 210px; }
  .divider { position: absolute; left: 326px; top: 30px; width: 1px; height: 110px; background: #c8d3e0; }
  .website { position: absolute; right: 20px; bottom: 14px; font-size: 14px; font-weight: 700; color: var(--navy); }

  /* back page */
  .back-photo { position: absolute; top: 0; left: 0; width: 100%; height: 246px; background: linear-gradient(120deg, #dfe6ec 0%, #b9c9d8 45%, #eef2f5 80%, #cdd8e2 100%); }
  .call-heading { position: absolute; top: 246px; left: 0; width: 100%; height: 80px; background: var(--white); border-radius: 40px 0 0 0; padding: 12px 0 0 90px; font-family: "PT Serif", Georgia, serif; font-weight: 700; text-transform: uppercase; line-height: 30px; }
  .call-heading .main { font-size: 27px; color: var(--navy); }
  .call-heading .sub { font-size: 23px; color: var(--blue); padding-left: 26px; }
  .benefits { position: absolute; top: 326px; left: 0; width: 100%; height: 132px; background: linear-gradient(var(--blue), var(--blue-deep)); padding: 14px 0 0 26px; color: var(--white); font-size: 17px; line-height: 26px; list-style: none; }
  .benefits li::before { content: "•"; margin-right: 8px; }
  .benefits .sep { margin: 0 8px; }
  .claims-seal { position: absolute; top: 342px; right: 22px; width: 96px; height: 96px; border-radius: 50%; background: var(--gold); border: 4px solid var(--white); color: var(--white); display: flex; flex-direction: column; justify-content: center; align-items: center; text-align: center; font-weight: 700; }
  .claims-seal .small { font-size: 8.5px; line-height: 10px; letter-spacing: .5px; }
  .claims-seal .big { font-size: 26px; line-height: 28px; }
  .carriers { position: absolute; top: 458px; left: 0; width: 100%; height: 60px; display: flex; justify-content: space-around; align-items: center; padding: 0 8px; font-size: 12px; font-weight: 700; color: var(--navy); }
  .back-footer { position: absolute; top: 576px; left: 0; width: 100%; height: 164px; }
  .back-footer .brand { left: 22px; top: 46px; width: 150px; font-size: 19px; line-height: 23px; }
  .contact { position: absolute; left: 210px; top: 40px; color: var(--navy); }
  .contact .phone { display: flex; align-items: center; gap: 8px; font-size: 24px; font-weight: 700; margin-bottom: 6px; }
  .contact .phone svg { width: 20px; height: 20px; fill: var(--blue); }
  .contact p { font-size: 13px; line-height: 18px; color: var(--grey-text); }
  .contact .agency { font-weight: 700; color: var(--navy); }
  .membership { position: absolute; right: 30px; top: 30px; width: 64px; height: 98px; border-radius: 6px; background: var(--navy); }
</style>
</head>
<body>

<svg width="0" height="0" style="position:absolute" aria-hidden="true">
  <defs>
    <symbol id="i-auto" viewBox="0 0 34 20"><path d="M3 14v-4l5-1 4-4h10l5 4 4 1v4z"/><circle cx="9" cy="15" r="3"/><circle cx="25" cy="15" r="3"/></symbol>
    <symbol id="i-home" viewBox="0 0 34 20"><path d="M17 1 6 10h3v9h6v-5h4v5h6v-9h3z"/></symbol>
    <symbol id="i-moto" viewBox="0 0 34 20"><circle cx="8" cy="14" r="4"/><circle cx="26" cy="14" r="4"/><path d="M8 13l6-6h6l4 2 2 5h-4l-3-3h-6z"/></symbol>
    <symbol id="i-boat" viewBox="0 0 34 20"><path d="M2 12h30l-5 6H7z"/><path d="M16 1v10h9z"/></symbol>
    <symbol id="i-rv" viewBox="0 0 34 20"><path d="M2 3h24l6 6v7H2z"/><circle cx="9" cy="16" r="3"/><circle cx="25" cy="16" r="3"/></symbol>
    <symbol id="i-truck" viewBox="0 0 34 20"><path d="M2 5h18v11H2zM21 8h6l5 5v3H21z"/><circle cx="8" cy="16" r="3"/><circle cx="26" cy="16" r="3"/></symbol>
  </defs>
</svg>

<section class="page page-front">
  <nav class="coverage-strip strip-top">
    <div class="item"><svg><use href="#i-auto"/></svg>AUTO</div>
    <div class="item"><svg><use href="#i-home"/></svg>HOME</div>
    <div class="item"><svg><use href="#i-moto"/></svg>MOTORCYCLE</div>
    <div class="item"><svg><use href="#i-boat"/></svg>BOAT</div>
    <div class="item"><svg><use href="#i-rv"/></svg>RV</div>
    <div class="item"><svg><use href="#i-truck"/></svg>TRUCK</div>
  </nav>

  <div class="hero">
    <div class="hero-photo" role="img" aria-label="Photo of a smiling family in front of a suburban house with a blue car parked beside them"></div>
    <h1 class="headline">
      <div class="line-one"><span class="accent">Why are you</span> paying so much <span class="accent">for</span></div>
      <div class="line-two">Auto Insurance?</div>
    </h1>
    <svg class="tagline-arc" viewBox="0 0 574 90">
      <defs><path id="arc-path" d="M70 78 Q300 10 560 48"/></defs>
      <text><textPath href="#arc-path">Let KRV lower your auto insurance bill!</textPath></text>
    </svg>
  </div>

  <div class="front-footer">
    <div class="method">
      <h3>How does KRV do it?</h3>
      <ul>
        <li>Find discounts you may be missing</li>
        <li>Comparison shop with multiple</li>
        <li>companies on your behalf</li>
        <li>Package policies for even more savings</li>
        <li>Find ways to reduce or eliminate fees</li>
      </ul>
    </div>
    <div class="promise">KRV has NO agency fees<br>Customize a policy just for you</div>
    <div class="divider"></div>
    <div class="brand"><span class="dot"></span><span>KRV Coverage Agency</span></div>
    <div class="website">www.krvcoverage.com</div>
  </div>
</section>

<section class="page page-back">
  <div class="back-photo" role="img" aria-label="Photo of a happy woman waving from the window of her car"></div>

  <h2 class="call-heading">
    <div class="main">Call KRV before paying</div>
    <div class="sub">your next insurance bill</div>
  </h2>

  <ul class="benefits">
    <li>Save money without cutting coverage or service</li>
    <li>Local Agent <span class="sep">•</span> Variety of discounts available</li>
    <li>Guaranteed claims repairs</li>
    <li>Friendly, knowledgeable agents</li>
  </ul>
  <div class="claims-seal"><span class="small">CLAIMS<br>SERVICE</span><span class="big">24/7</span></div>

  <div class="carriers">
    <span>Lakemount</span>
    <span>Harbridge Auto &amp; Home</span>
    <span>Dunmarrow Insurance</span>
    <span>Alpenrow</span>
    <span>Westmere Insurance</span>
  </div>

  <nav class="coverage-strip strip-dark">
    <div class="item"><svg><use href="#i-auto"/></svg>AUTO</div>
    <div class="item"><svg><use href="#i-home"/></svg>HOME</div>
    <div class="item"><svg><use href="#i-moto"/></svg>MOTORCYCLE</div>
    <div class="item"><svg><use href="#i-boat"/></svg>BOAT</div>
    <div class="item"><svg><use href="#i-rv"/></svg>RV</div>
    <div class="item"><svg><use href="#i-truck"/></svg>TRUCK</div>
  </nav>

  <div class="back-footer">
    <div class="brand"><span class="dot"></span><span>KRV Coverage Agency</span></div>
    <div class="contact">
      <div class="phone"><svg viewBox="0 0 24 24"><path d="M6.6 10.8a15 15 0 0 0 6.6 6.6l2.2-2.2a1 1 0 0 1 1-.25 11.4 11.4 0 0 0 3.6.57 1 1 0 0 1 1 1V20a1 1 0 0 1-1 1A17 17 0 0 1 3 4a1 1 0 0 1 1-1h3.5a1 1 0 0 1 1 1c0 1.25.2 2.45.57 3.57a1 1 0 0 1-.25 1z"/></svg>(555) 014-2780</div>
      <p class="agency">KRV Coverage Agency</p>
      <p>2210-B Harlow Creek Rd.</p>
      <p>Alderton, NC 28000</p>
      <p>www.krvcoverage.com</p>
    </div>
    <div class="membership" role="img" aria-label="CMQ member badge"></div>
  </div>
</section>

</body>
</html>
```